" Ponte Dourada é uma loja de artigos religiosos católicos em fase instalação em Brasília - DF, dedicada a oferecer produtos que fortalecem a espiritualidade dos fiéis. A proposta é comercializar terços, imagens sacras, livros, bíblias e artigos litúrgicos em loja física e futuramente online. O diferencial são os produtos personalizados e a implantação de um espaço devocional. A empresa visa tornar-se referência no segmento em nível regional, nacional e online. "

```html
<!DOCTYPE html>
<html lang="pt-BR">
<head>
<meta charset="UTF-8">
<title>Ponte Dourada – Faixa de vitrine</title>
<link rel="stylesheet" href="https://fonts.googleapis.com/css2?family=Cinzel:wght@500&family=Montserrat:wght@500&display=swap">
<style>
  :root {
    --canvas-bg: #eceeef;
    --navy: #1d2a44;
    --navy-deep: #17223a;
    --gold: #c9a45a;
    --gold-light: #e2c27c;
    --white: #ffffff;
  }
  html, body {
    margin: 0;
    padding: 0;
    width: 1200px;
    height: 1200px;
    overflow: hidden;
    background: var(--canvas-bg);
  }
  .canvas {
    position: relative;
    width: 1200px;
    height: 1200px;
    display: flex;
    align-items: center;
  }
  .window-band {
    position: relative;
    width: 100%;
    height: 250px;
    background: var(--navy);
    border-top: 8px solid var(--gold);
    border-bottom: 8px solid var(--gold);
    box-sizing: border-box;
  }
  .band-texture {
    position: absolute;
    inset: 0;
    background: linear-gradient(90deg, var(--navy-deep), var(--navy) 50%, var(--navy-deep));
    opacity: 0.6;
  }
  .contact {
    position: absolute;
    left: 90px;
    top: 50%;
    transform: translateY(-50%);
    display: flex;
    align-items: center;
    gap: 22px;
  }
  .contact-icon {
    width: 58px;
    height: 58px;
  }
  .contact-phone {
    font-family: "Montserrat", sans-serif;
    font-weight: 500;
    font-size: 46px;
    color: var(--white);
    letter-spacing: 0.5px;
  }
  .brand {
    position: absolute;
    left: 680px;
    top: 50%;
    transform: translateY(-50%);
    display: flex;
    align-items: center;
    gap: 26px;
  }
  .brand-dot {
    width: 22px;
    height: 22px;
    border-radius: 50%;
    background: var(--gold-light);
  }
  .brand-name {
    font-family: "Cinzel", serif;
    font-weight: 500;
    font-size: 56px;
    color: var(--gold-light);
    letter-spacing: 1px;
  }
</style>
</head>
<body>
<main class="canvas">
  <section class="window-band">
    <div class="band-texture" role="img" aria-label="Padrão discreto de símbolos religiosos repetidos sobre o fundo azul"></div>

    <div class="contact">
      <svg class="contact-icon" viewBox="0 0 58 58" aria-hidden="true">
        <circle cx="29" cy="29" r="27" fill="none" stroke="var(--gold-light)" stroke-width="4"/>
        <path d="M21 17c-2 0-4 2-4 5 0 9 10 19 19 19 3 0 5-2 5-4v-3l-6-3-3 3c-4-2-6-4-8-8l3-3-3-6z" fill="var(--gold-light)"/>
      </svg>
      <span class="contact-phone">(61) 9 0000.0000</span>
    </div>

    <div class="brand">
      <span class="brand-dot" aria-hidden="true"></span>
      <span class="brand-name">Ponte Dourada</span>
    </div>
  </section>
</main>
</body>
</html>
```